Crestline Lending Group Business Cards

We are looking to revamp the current business cards each of our locations uses. We are a lending company that specializes in personal loans, title loans, and tax services. We have locations in New Mexico, Texas, and Oklahoma.

We would like a cleaner, sleeker look while still highlighting what we offer. Title Loans, Personal Loans & Tax Services. We also want to include our referral fee somewhere on the card. We would like to see an English option as well as a Spanish option for the cards.

PLEASE NOTE: Some business cards do not include the employee's name but just the store's location, while others will include both.

These are double-sided business cards, and we would like to see proof if possible. I have included proofs of our current business cards for you to review below, as well as our company logo. Feel free to get creative with the logo, etc! Colors should match the logo; however, you do not need to use all of our logo colors if you don't want to.

```html
<!DOCTYPE html>
<html lang="en">
<head>
<meta charset="utf-8">
<title>Crestline Lending Group – Business Card</title>
<link rel="stylesheet" href="https://fonts.googleapis.com/css2?family=Poppins:wght@400;500;600;700;800&display=swap">
<style>
  :root {
    --brand-red: #c1232a;
    --brand-green: #13502f;
    --paper: #ffffff;
    --page: #ffffff;
  }
  * { box-sizing: border-box; margin: 0; padding: 0; }
  html, body {
    width: 943px; height: 1200px; overflow: hidden;
    background: var(--page);
    font-family: "Poppins", sans-serif;
  }
  .sheet { position: relative; width: 943px; height: 1200px; }

  .card {
    position: absolute; left: 105px; width: 735px; height: 451px;
    background: var(--paper); overflow: hidden;
    box-shadow: 0 6px 22px rgba(0,0,0,0.10);
  }
  .card--front { top: 117px; }
  .card--back { top: 637px; }
  .card__waves { position: absolute; inset: 0; width: 100%; height: 100%; }

  /* front */
  .store-icon { position: absolute; left: 59px; top: 44px; width: 67px; height: 57px; }
  .address { position: absolute; left: 63px; top: 104px; font-weight: 600; font-size: 25px; line-height: 31px; }
  .address__street { color: var(--brand-red); }
  .address__city { color: var(--brand-green); }
  .address__rule { position: absolute; left: 63px; top: 173px; width: 78px; height: 3px; background: var(--brand-red); }

  .contact { position: absolute; left: 57px; top: 241px; list-style: none; }
  .contact__item { display: flex; align-items: center; height: 29px; color: var(--brand-green); }
  .contact__icon { width: 25px; height: 25px; margin-right: 8px; flex: none; }
  .contact__item--phone { font-size: 19px; font-weight: 600; }
  .contact__item--email { font-size: 16.5px; font-weight: 500; }

  .website { position: absolute; left: 37px; top: 389px; font-size: 20px; font-weight: 700; color: var(--paper); }

  .brand-name {
    position: absolute; text-align: center; font-weight: 600; line-height: 1.05;
  }
  .brand-name--front { right: 34px; top: 52px; width: 240px; color: var(--brand-green); font-size: 36px; }
  .brand-name--back { left: 40px; top: 272px; width: 270px; color: var(--paper); font-size: 36px; }

  /* back */
  .referral-ribbon {
    position: absolute; left: -4px; top: 50px; width: 260px;
    transform: rotate(-29.6deg); transform-origin: center;
    color: var(--paper); font-size: 32px; font-weight: 500; text-align: center; white-space: nowrap;
  }
  .offer__get { position: absolute; left: 273px; top: 44px; font-size: 62px; font-weight: 800; color: var(--brand-green); letter-spacing: -2px; line-height: 1; }
  .offer__upto { position: absolute; left: 324px; top: 100px; font-size: 22px; font-weight: 400; color: var(--brand-green); line-height: 1; }
  .offer__amount { position: absolute; left: 394px; top: 26px; font-size: 124px; font-weight: 800; color: var(--brand-red); letter-spacing: -2px; line-height: 1; }

  .services { position: absolute; left: 458px; top: 304px; list-style: none; }
  .services__item { display: flex; align-items: center; height: 38px; color: var(--paper); font-size: 22.5px; font-weight: 600; }
  .services__arrow { width: 22px; height: 16px; margin-right: 6px; flex: none; }
</style>
</head>
<body>
<div class="sheet">

  <!-- Front -->
  <section class="card card--front">
    <svg class="card__waves" viewBox="0 0 1325 812" preserveAspectRatio="none" aria-hidden="true">
      <path fill="var(--brand-red)" d="M0,695 C200,600 380,615 560,660 C720,700 850,702 1000,680 C1150,652 1250,592 1325,530 L1325,668 C1260,700 1180,745 1050,765 C850,790 650,720 450,670 C300,640 150,630 0,695 Z"/>
      <path fill="var(--brand-green)" d="M0,695 C150,630 300,640 450,670 C650,720 850,790 1050,765 C1180,745 1260,700 1325,668 L1325,812 L0,812 Z"/>
      <path fill="var(--brand-red)" d="M500,633 C800,630 1150,560 1325,325 L1325,460 C1200,580 1000,662 800,657 C680,654 580,646 500,633 Z"/>
    </svg>

    <svg class="store-icon" viewBox="0 0 120 100" aria-hidden="true">
      <path fill="var(--brand-red)" d="M14,0 H106 L120,30 Q120,40 110,40 Q100,40 96,32 Q92,40 84,40 Q74,40 72,32 Q68,40 60,40 Q50,40 48,32 Q44,40 36,40 Q26,40 24,32 Q20,40 10,40 Q0,40 0,30 Z"/>
      <path fill="var(--brand-green)" d="M10,46 H110 V100 H10 Z"/>
      <rect x="24" y="62" width="38" height="16" fill="var(--paper)"/>
      <rect x="74" y="62" width="18" height="34" fill="var(--paper)"/>
    </svg>

    <div class="address">
      <p class="address__street">318 Cedar Avenue</p>
      <p class="address__city">Millbrook, Texas 78021</p>
    </div>
    <div class="address__rule"></div>

    <ul class="contact">
      <li class="contact__item contact__item--phone">
        <svg class="contact__icon" viewBox="0 0 24 24" aria-hidden="true">
          <circle cx="12" cy="12" r="11" fill="none" stroke="var(--brand-red)" stroke-width="1.3"/>
          <path fill="var(--brand-red)" d="M8.2,6.5 L10,8.8 L9,10.2 Q10.3,12.8 13,14.2 L14.4,13.2 L16.7,15 L15.6,17 Q11,16.6 8,12.4 Q6.6,9.6 7,7.4 Z"/>
        </svg>
        (575) 482-3096
      </li>
      <li class="contact__item contact__item--email">
        <svg class="contact__icon" viewBox="0 0 24 24" aria-hidden="true">
          <circle cx="12" cy="12" r="11" fill="none" stroke="var(--brand-red)" stroke-width="1.3"/>
          <rect x="6" y="8" width="12" height="8.5" fill="var(--brand-red)"/>
          <path d="M6.5,8.5 L12,13 L17.5,8.5 M6.5,16 L10.5,12 M17.5,16 L13.5,12" fill="none" stroke="var(--paper)" stroke-width="0.9"/>
        </svg>
        info@crestlinelending.com
      </li>
    </ul>

    <p class="brand-name brand-name--front">Crestline Lending Group</p>

    <p class="website">www.crestlinelending.com</p>
  </section>

  <!-- Back -->
  <section class="card card--back">
    <svg class="card__waves" viewBox="0 0 1322 812" preserveAspectRatio="none" aria-hidden="true">
      <polygon fill="var(--brand-red)" points="0,227 400,0 595,0 0,334"/>
      <path fill="var(--brand-red)" d="M0,422 C200,335 380,345 560,395 C720,438 860,440 1010,418 C1150,395 1250,440 1322,367 L1322,492 C1260,525 1180,552 1010,557 C830,560 650,480 450,440 C300,410 150,395 0,422 Z"/>
      <path fill="var(--brand-green)" d="M0,422 C150,395 300,410 450,440 C650,480 830,560 1010,557 C1180,552 1260,525 1322,492 L1322,812 L0,812 Z"/>
      <path fill="var(--brand-red)" d="M540,385 C850,400 1150,360 1322,197 L1322,282 C1200,390 1000,445 800,430 C680,420 600,400 540,385 Z"/>
    </svg>

    <p class="referral-ribbon">Refer a Friend</p>

    <div class="offer">
      <span class="offer__get">GET</span>
      <span class="offer__upto">up to</span>
      <span class="offer__amount">$100</span>
    </div>

    <p class="brand-name brand-name--back">Crestline Lending Group</p>

    <ul class="services">
      <li class="services__item">
        <svg class="services__arrow" viewBox="0 0 22 16" aria-hidden="true">
          <rect x="0" y="4" width="2" height="8" fill="var(--paper)"/>
          <rect x="4" y="4" width="2" height="8" fill="var(--paper)"/>
          <rect x="8" y="4" width="2" height="8" fill="var(--paper)"/>
          <path d="M12,0 L22,8 L12,16 Z" fill="var(--paper)"/>
        </svg>
        Personal Loans
      </li>
      <li class="services__item">
        <svg class="services__arrow" viewBox="0 0 22 16" aria-hidden="true">
          <rect x="0" y="4" width="2" height="8" fill="var(--paper)"/>
          <rect x="4" y="4" width="2" height="8" fill="var(--paper)"/>
          <rect x="8" y="4" width="2" height="8" fill="var(--paper)"/>
          <path d="M12,0 L22,8 L12,16 Z" fill="var(--paper)"/>
        </svg>
        Title Loans
      </li>
      <li class="services__item">
        <svg class="services__arrow" viewBox="0 0 22 16" aria-hidden="true">
          <rect x="0" y="4" width="2" height="8" fill="var(--paper)"/>
          <rect x="4" y="4" width="2" height="8" fill="var(--paper)"/>
          <rect x="8" y="4" width="2" height="8" fill="var(--paper)"/>
          <path d="M12,0 L22,8 L12,16 Z" fill="var(--paper)"/>
        </svg>
        Tax Services
      </li>
    </ul>
  </section>

</div>
</body>
</html>
```